Managed Service provider for IT support needs a three panel fold flyer

We are a Information & Technology company, providing compelte managed services ot the SMB market in southern Califonia.
Looking for a three panel, tri-fold or other, 3.75 X 8.35 Vertical flyer.
The final design should communicate a partnered techjnology solution

Managed Services:
Designed to reduce your costs, increase your profits and mitigate your business risks, we partner with you as your Virtual IT Department, allowing you to focus on running your business, not your technology.

https://verolinkzo.com/

It Company

```html
<!DOCTYPE html>
<html lang="en">
<head>
<meta charset="utf-8">
<title>Verolinkzo Computer Service – Tri-fold Brochure</title>
<link href="https://fonts.googleapis.com/css2?family=Open+Sans:ital,wght@0,400;0,600;0,700;1,400&display=swap" rel="stylesheet">
<style>
:root{
  --blue:#0e6fbd;
  --blue-dark:#0a4f8f;
  --navy:#1d2a3c;
  --ink:#222;
  --grey-text:#333;
  --paper:#ffffff;
  --panel-grey:#eceef1;
  --stage:#e9ebee;
  --font:"Open Sans", Arial, sans-serif;
}
*{box-sizing:border-box;margin:0;padding:0}
html,body{width:1200px;height:1200px;overflow:hidden;background:var(--stage);font-family:var(--font);color:var(--ink)}
.spread{position:absolute;left:210px;width:780px;height:578px;background:var(--paper);display:flex;box-shadow:0 2px 10px rgba(0,0,0,.15)}
.spread--inside{top:14px}
.spread--outside{top:608px}
.panel{position:relative;width:260px;height:578px;overflow:hidden}
.panel + .panel{border-left:1px solid #e2e4e8}

/* Inside left: expertise */
.expertise{background:linear-gradient(160deg,#f4f5f7,#e3e6ea)}
.expertise__title{position:absolute;top:34px;left:24px;font-size:26px;font-weight:700;color:var(--blue)}
.expertise__band{position:absolute;left:0;width:260px;height:112px}
.expertise__photo{position:absolute;inset:0}
.expertise__label{position:absolute;left:0;bottom:0;background:var(--blue);color:#fff;font-size:13px;padding:5px 26px 5px 16px;border-radius:0 18px 0 0}
.band-1{top:92px}.band-2{top:210px}.band-3{top:328px}.band-4{top:446px}
.band-1 .expertise__photo{background:linear-gradient(120deg,#5a6470,#b9c0c8 60%,#3d4653)}
.band-2 .expertise__photo{background:radial-gradient(circle at 60% 40%,#4aa3e6,#0d3f78 75%)}
.band-3 .expertise__photo{background:linear-gradient(120deg,#2f86d1,#9dd0f2 55%,#1b5fa3)}
.band-4 .expertise__photo{background:linear-gradient(130deg,#7b8894,#2b3340 55%,#c98a4a)}

/* Inside services header */
.services{width:520px;position:relative}
.services__header{position:absolute;top:0;left:0;width:520px;height:118px;background:linear-gradient(180deg,#2b3d55,#6d8199 70%,#e9edf2)}
.services__pill{position:absolute;top:44px;left:40px;width:440px;height:56px;background:var(--navy);border-radius:28px;color:#fff;text-align:center;padding-top:6px}
.services__pill h2{font-size:22px;font-weight:700}
.services__pill p{font-size:10px}
.services__cols{position:absolute;top:132px;left:0;width:520px;display:flex}
.services__col{width:260px;padding:0 20px}
.service{margin-bottom:20px}
.service h3{color:var(--blue);font-size:16px;font-weight:700;margin-bottom:6px}
.service p{font-size:10.5px;line-height:1.45;color:var(--grey-text)}

/* Outside left flap */
.flap__photo-top{position:absolute;top:0;left:0;width:260px;height:200px;background:linear-gradient(180deg,#f2f4f6,#d8dde2)}
.flap__band{position:absolute;top:200px;left:0;width:260px;height:110px;background:var(--blue);color:#fff;font-weight:700;font-size:17px;line-height:1.35;padding:24px 20px}
.flap__photo-bottom{position:absolute;top:310px;left:0;width:260px;height:268px;background:linear-gradient(160deg,#e6eaee,#9aa4ae 55%,#3a4350)}

/* Outside middle: contact */
.contact__photo{position:absolute;top:0;left:0;width:260px;height:300px;background:linear-gradient(170deg,#f3f5f7,#c6cdd4 60%,#8d98a3)}
.contact__body{position:absolute;top:300px;left:0;width:260px;height:278px;background:var(--blue);color:#fff;padding:26px 22px}
.contact__title{font-size:22px;font-weight:700;margin-bottom:20px}
.contact__row{display:flex;align-items:center;gap:10px;font-size:13px;margin-bottom:14px}
.contact__row svg{width:18px;height:18px;flex:none}
.contact__web{margin-top:36px;font-size:16px;font-weight:700}

/* Cover */
.cover__brand{position:absolute;top:22px;left:0;width:260px;text-align:center}
.cover__name{display:inline-flex;align-items:center;gap:8px;font-size:30px;font-weight:700;color:var(--blue)}
.cover__name i{display:inline-block;width:14px;height:14px;background:var(--blue)}
.cover__sub{font-size:10px;letter-spacing:5px;color:var(--blue);margin-top:-2px}
.cover__tagline{font-size:9.5px;font-style:italic;margin-top:8px}
.cover__photo{position:absolute;top:118px;left:0;width:260px;height:210px;background:linear-gradient(120deg,#5c6672,#c9d0d7 55%,#f1e4da)}
.cover__title{position:absolute;top:346px;left:20px;font-size:27px;font-weight:700;line-height:1.15;color:var(--ink)}
.cover__lede{position:absolute;top:500px;left:20px;width:225px;font-size:11px;line-height:1.4}
</style>
</head>
<body>

<section class="spread spread--inside">
  <div class="panel expertise">
    <h2 class="expertise__title">Our Expertise</h2>
    <div class="expertise__band band-1"><div class="expertise__photo" role="img" aria-label="Photo of a woman using a tablet beside server racks"></div><span class="expertise__label">Cloud Solutions</span></div>
    <div class="expertise__band band-2"><div class="expertise__photo" role="img" aria-label="Illustration of a network of connected people icons"></div><span class="expertise__label">Unified Communications</span></div>
    <div class="expertise__band band-3"><div class="expertise__photo" role="img" aria-label="Illustration of device and security icons"></div><span class="expertise__label">Security</span></div>
    <div class="expertise__band band-4"><div class="expertise__photo" role="img" aria-label="Photo of a hand holding a smartphone"></div><span class="expertise__label">Mobility</span></div>
  </div>

  <div class="services">
    <div class="services__header" role="img" aria-label="Photo of an office interior in blue tones"></div>
    <div class="services__pill">
      <h2>Some of our Services</h2>
      <p>We tailor our cost-effective IT services and solutions to meet your specific business needs</p>
    </div>
    <div class="services__cols">
      <div class="services__col">
        <article class="service">
          <h3>Managed IT Services</h3>
          <p>We deliver proactive flat-rate Managed IT Services in Corvale, CA. Designed to reduce your costs, eliminate business pain, increase your profits and mitigate business risks, we partner with you as your Virtual IT Department and outsourced CTO, allowing you to focus on running your business, not your technology.</p>
        </article>
        <article class="service">
          <h3>Healthcare IT Services</h3>
          <p>Do you need a HIPAA and HITECH compliant Healthcare IT partner? Does your practice need EHR and Practice Management support? Would you like secure, fast and compliant systems? Our Healthcare IT services in Corvale, CA are built for you.</p>
        </article>
      </div>
      <div class="services__col">
        <article class="service">
          <h3>Manufacturing IT Services</h3>
          <p>Do you need an IT firm experienced in supporting your manufacturing processes, equipment and specialized line of business applications? Our manufacturing IT services in Corvale, CA include remote and onsite system and software support, 24×7 network monitoring, patching and updating and more.</p>
        </article>
        <article class="service">
          <h3>Finance IT Services</h3>
          <p>Do you need an IT firm experienced in the regulations of your financial line of business applications? Would you like stronger security and a reliable network? Our Finance IT solutions in Corvale, CA deliver.</p>
        </article>
        <article class="service">
          <h3>Legal IT Services</h3>
          <p>Do you need an IT firm versed in legal processes and e-discovery, archiving and document management? Increase availability of your critical data and services with our Legal IT solutions in Corvale, CA.</p>
        </article>
      </div>
    </div>
  </div>
</section>

<section class="spread spread--outside">
  <div class="panel flap">
    <div class="flap__photo-top" role="img" aria-label="Photo of a bright office workspace"></div>
    <div class="flap__band">Find out how our IT Solutions can help your organization!</div>
    <div class="flap__photo-bottom" role="img" aria-label="Photo of laptops on an office desk"></div>
  </div>

  <div class="panel contact">
    <div class="contact__photo" role="img" aria-label="Photo of an office with laptop screens"></div>
    <div class="contact__body">
      <h2 class="contact__title">Contact Us</h2>
      <div class="contact__row">
        <svg viewBox="0 0 24 24" aria-hidden="true"><path fill="#fff" d="M6.6 10.8a15 15 0 0 0 6.6 6.6l2.2-2.2c.3-.3.7-.4 1-.2 1.1.4 2.3.6 3.6.6.6 0 1 .4 1 1V20c0 .6-.4 1-1 1A17 17 0 0 1 3 4c0-.6.4-1 1-1h3.5c.6 0 1 .4 1 1 0 1.3.2 2.5.6 3.6.1.3 0 .7-.2 1z"/></svg>
        <span>(555) 014-2276</span>
      </div>
      <div class="contact__row">
        <svg viewBox="0 0 24 24" aria-hidden="true"><rect x="2" y="5" width="20" height="14" rx="1" fill="#fff"/><path d="M2 6l10 7 10-7" stroke="#0e6fbd" stroke-width="1.8" fill="none"/></svg>
        <span>hello@verolinkzo.com</span>
      </div>
      <p class="contact__web">https://verolinkzo.com/</p>
    </div>
  </div>

  <div class="panel cover">
    <div class="cover__brand">
      <div class="cover__name"><i></i>Verolinkzo</div>
      <div class="cover__sub">computer service</div>
      <p class="cover__tagline">“Timely IT support to power your Business”</p>
    </div>
    <div class="cover__photo" role="img" aria-label="Photo of a smiling support agent wearing a headset with colleagues behind"></div>
    <h1 class="cover__title">Technology<br>Management<br>Consulting<br>Services</h1>
    <p class="cover__lede">Delivering quality IT solutions, support and services tailored to your specific business needs</p>
  </div>
</section>

</body>
</html>
```